Design a Mothers day Promotional Banner for a spa

Velvet Harbor Spa needs a new advertisement banner for advertising on Chatterloop and possibly some other websites.

The banner is to promote the new deal on Mothers Day for a limited time only.

Here is the website for all the info you need.

here is the quib account

Feel free to use nice stock images or if you think you can work with the website gallery images, you can use them.

We need the banner to have a nice classy and sexy graphic in it. It should look really inviting and pleasing.

The banner needs to have the spa address and phone number in it but make sure to keep it classy and not make it cheesy.

The banner size should be at least 1200x900px
Feel free to deliver in other dimensions as well.
Final Advice:
Be creative and have fun with it.

Here is the content you should use to offer text
==========================================

Happy Mother's Day Promotion:
[login to view URL] massage :$10 off (Original price:$60/hours)
[login to view URL] Medicine Meridian Massage $10 off (Original price:$60/hour)
3. Anti-aging skin care $10 off (original price:$60/hour)

============================================
Feel free to modify the text to make it more apealing and look proffesional.

```html
<!DOCTYPE html>
<html lang="en">
<head>
<meta charset="utf-8">
<title>Velvet Harbor Spa – Mother's Day Promotion</title>
<link rel="stylesheet" href="https://fonts.googleapis.com/css2?family=Great+Vibes&family=Montserrat:wght@500;600&display=swap">
<style>
  :root {
    --rose-deep: #6e0a10;
    --rose: #a3141c;
    --linen: #efe9e2;
    --linen-warm: #d9cfc4;
    --maroon-dark: #2a0508;
    --maroon: #7a0f14;
    --leaf-dark: #3e8a1c;
    --leaf: #76be3a;
    --leaf-light: #a9d86e;
    --ink-green: #1f3d0c;
    --white: #ffffff;
    --contact: #8a1a1a;
  }
  * { margin: 0; padding: 0; box-sizing: border-box; }
  html, body { width: 1200px; height: 900px; overflow: hidden; background: var(--white); }
  .banner { position: relative; width: 1200px; height: 900px; overflow: hidden; }

  .backdrop {
    position: absolute; inset: 0;
    background:
      radial-gradient(ellipse 260px 240px at 780px 200px, var(--rose) 0%, var(--rose-deep) 55%, transparent 100%),
      radial-gradient(ellipse 520px 260px at 180px 120px, #7d1218 0%, transparent 100%),
      linear-gradient(170deg, #8e1e22 0%, #c9b8aa 38%, var(--linen) 60%, var(--linen-warm) 100%);
  }

  .headline {
    position: absolute; top: 40px; left: 0; width: 1200px;
    text-align: center; color: var(--white);
    font-family: "Great Vibes", cursive; font-weight: 400;
    text-shadow: 2px 3px 6px rgba(60, 0, 0, .55);
  }
  .headline .line-1 { display: block; font-size: 118px; line-height: 1.05; }
  .headline .line-2 { display: block; font-size: 118px; line-height: 1.05; }

  .discount-tag { position: absolute; left: 0; top: 406px; width: 570px; height: 174px; }
  .discount-text {
    position: absolute; left: 48px; top: 406px; height: 174px;
    display: flex; align-items: center;
    font-family: "Montserrat", sans-serif; font-weight: 600;
    font-size: 86px; color: var(--white); letter-spacing: 1px;
  }

  .service { position: absolute; right: 0; width: 520px; }
  .service svg { position: absolute; inset: 0; width: 100%; height: 100%; }
  .service-text {
    position: relative; height: 100%;
    display: flex; flex-direction: column; justify-content: center; align-items: flex-end;
    padding-right: 36px; text-align: right;
    font-family: "Great Vibes", cursive; color: var(--white);
    text-shadow: 1px 1px 0 var(--ink-green), -1px -1px 0 var(--ink-green), 1px -1px 0 var(--ink-green), -1px 1px 0 var(--ink-green), 2px 3px 4px rgba(0,0,0,.35);
  }
  .service-name { font-size: 50px; line-height: 1.05; }
  .service-price { font-size: 38px; line-height: 1.2; }
  .service--massage { top: 344px; height: 150px; }
  .service--skin { top: 498px; height: 150px; }
  .service--meridian { top: 652px; height: 150px; }
  .service--meridian .service-name { font-size: 44px; }

  .footer {
    position: absolute; left: 0; bottom: 0; width: 1200px; height: 100px;
    background: linear-gradient(180deg, var(--leaf-light) 0%, var(--leaf) 55%, #5fa52a 100%);
  }
  .contact {
    position: absolute; left: 106px; top: 12px;
    font-family: "Montserrat", sans-serif; font-weight: 500; font-size: 19px;
    color: var(--contact); list-style: none;
  }
  .contact li { display: flex; align-items: center; height: 38px; }
  .contact svg { position: absolute; left: -38px; width: 22px; height: 22px; }
  .brand {
    position: absolute; right: 60px; top: 20px;
    display: flex; align-items: center; gap: 14px;
    font-family: "Great Vibes", cursive; font-size: 52px; color: var(--maroon);
  }
  .brand-dot { width: 34px; height: 34px; border-radius: 50%; background: var(--maroon); }
</style>
</head>
<body>
<main class="banner">
  <div class="backdrop" role="img" aria-label="Soft-focus photo of a red rose resting on a folded white spa towel"></div>

  <h1 class="headline">
    <span class="line-1">Happy Mother's Day</span>
    <span class="line-2">Promotion</span>
  </h1>

  <svg class="discount-tag" viewBox="0 0 570 174" aria-hidden="true">
    <defs>
      <linearGradient id="tag-fill" x1="0" x2="1" y1="0" y2="0">
        <stop offset="0" stop-color="#1e0306"/>
        <stop offset=".7" stop-color="#5a0b10"/>
        <stop offset="1" stop-color="#8a151a"/>
      </linearGradient>
    </defs>
    <polygon points="0,0 510,0 570,87 510,174 0,174" fill="url(#tag-fill)"/>
  </svg>
  <div class="discount-text">$ 10 OFF</div>

  <div class="service service--massage">
    <svg viewBox="0 0 520 150" preserveAspectRatio="none" aria-hidden="true">
      <defs>
        <linearGradient id="ribbon" x1="0" x2="1" y1="0" y2="1">
          <stop offset="0" stop-color="#3c8a1a"/>
          <stop offset=".45" stop-color="#7cc23c"/>
          <stop offset="1" stop-color="#4e9a22"/>
        </linearGradient>
      </defs>
      <polygon points="0,0 520,0 520,150 30,150 0,75" fill="url(#ribbon)"/>
    </svg>
    <div class="service-text">
      <span class="service-name">Therapeutic massage</span>
      <span class="service-price">(Original price $60/ hours)</span>
    </div>
  </div>

  <div class="service service--skin">
    <svg viewBox="0 0 520 150" preserveAspectRatio="none" aria-hidden="true">
      <polygon points="0,0 520,0 520,150 30,150 0,75" fill="url(#ribbon)"/>
    </svg>
    <div class="service-text">
      <span class="service-name">Anti-aging skin care</span>
      <span class="service-price">(Original price $60/ hours)</span>
    </div>
  </div>

  <div class="service service--meridian">
    <svg viewBox="0 0 520 150" preserveAspectRatio="none" aria-hidden="true">
      <polygon points="0,0 520,0 520,150 30,150 0,75" fill="url(#ribbon)"/>
    </svg>
    <div class="service-text">
      <span class="service-name">Chinese Medicine Meridian<br>Massage</span>
      <span class="service-price">(Original price $60/ hours)</span>
    </div>
  </div>

  <footer class="footer">
    <ul class="contact">
      <li>
        <svg viewBox="0 0 24 24" aria-hidden="true"><path fill="#8a1a1a" d="M6.6 10.8a15 15 0 0 0 6.6 6.6l2.2-2.2a1 1 0 0 1 1-.25 11.4 11.4 0 0 0 3.6.6 1 1 0 0 1 1 1V20a1 1 0 0 1-1 1A17 17 0 0 1 3 4a1 1 0 0 1 1-1h3.5a1 1 0 0 1 1 1c0 1.25.2 2.45.6 3.6a1 1 0 0 1-.25 1z"/></svg>
        555-204-7316
      </li>
      <li>
        <svg viewBox="0 0 24 24" aria-hidden="true"><path fill="#8a1a1a" d="M12 2a7 7 0 0 0-7 7c0 5.2 7 13 7 13s7-7.8 7-13a7 7 0 0 0-7-7zm0 9.5A2.5 2.5 0 1 1 12 6.5a2.5 2.5 0 0 1 0 5z"/></svg>
        48 MARLOW CREST AVE., ALDEN BAY, CA 90911
      </li>
    </ul>
    <div class="brand"><span class="brand-dot"></span>Velvet Harbor Spa</div>
  </footer>
</main>
</body>
</html>
```